design a construction company business card

Design business card around our logo. Card must have all the typical info: name, title, address, phone, email, business name, etc. Somewhere on the card I would like to see our motto "Built on integrity... Inspired by commitment." Consider adding a splash of bright orange to the card to complement the blues and silvers/grays in the logo. We are open to metallic inks, textures, etc. We would like to see options on both light and dark backgrounds. The font in the logo is Euro Technic Extended Regular.

```html
<!DOCTYPE html>
<html lang="en">
<head>
<meta charset="utf-8">
<title>Halden Contracting – Business Card</title>
<link href="https://fonts.googleapis.com/css2?family=Michroma&display=swap" rel="stylesheet">
<style>
  :root {
    --backdrop: #2b2b2b;
    --card: #ffffff;
    --ink: #4a4a4a;
    --ink-soft: #5e5e5e;
    --blue: #1f6fc4;
    --logo-blue: #2450b0;
  }
  * { margin: 0; padding: 0; box-sizing: border-box; }
  html, body {
    width: 1200px; height: 901px; overflow: hidden;
    background: var(--backdrop);
    font-family: "Michroma", sans-serif;
  }
  .card {
    position: absolute; left: 250px; width: 700px; height: 400px;
    background: var(--card);
    box-shadow: 0 6px 18px rgba(0,0,0,.45);
    overflow: hidden;
  }
  .card-front { top: 38px; }
  .card-back { top: 466px; }

  /* front */
  .brand {
    position: absolute; left: 0; right: 0; top: 128px;
    text-align: center; color: var(--logo-blue);
  }
  .brand-name { font-size: 46px; letter-spacing: 3px; line-height: 1; }
  .brand-sub { font-size: 15px; letter-spacing: 2px; margin-top: 10px; }
  .motto {
    position: absolute; left: 0; right: 0; top: 300px;
    text-align: center; font-size: 13px; color: var(--ink-soft); letter-spacing: .5px;
  }

  /* back */
  .identity {
    position: absolute; right: 370px; top: 150px; text-align: right;
  }
  .person-name { font-size: 27px; color: var(--ink); letter-spacing: -.5px; font-weight: 700; }
  .person-title { font-size: 17px; color: var(--blue); margin-top: 6px; }
  .divider {
    position: absolute; left: 346px; top: 150px; width: 1.5px; height: 72px; background: var(--ink);
  }
  .contacts {
    position: absolute; left: 366px; top: 152px; list-style: none;
    font-size: 14px; color: var(--ink); line-height: 23px;
  }
  .contacts li { display: flex; align-items: center; gap: 10px; }
  .contacts svg { width: 12px; height: 12px; fill: var(--blue); flex: none; }
  .contacts .accent { color: var(--blue); }
  .address {
    position: absolute; left: 90px; top: 318px;
    display: flex; align-items: center; gap: 8px;
    font-size: 14px; color: var(--ink);
  }
  .address svg { width: 12px; height: 16px; fill: var(--blue); }
  .edge-band {
    position: absolute; left: 0; right: 0; bottom: 0; height: 8px; background: var(--blue);
  }
</style>
</head>
<body>
  <section class="card card-front">
    <div class="brand">
      <div class="brand-name">HALDEN</div>
      <div class="brand-sub">CONTRACTING, INC.</div>
    </div>
    <p class="motto">"Built on integrity... Inspired by commitment."</p>
  </section>

  <section class="card card-back">
    <div class="identity">
      <div class="person-name">DANIEL BROOKS</div>
      <div class="person-title">Ceo &amp; Founder</div>
    </div>
    <div class="divider"></div>
    <ul class="contacts">
      <li><svg viewBox="0 0 24 24"><path d="M6.6 10.8a15 15 0 0 0 6.6 6.6l2.2-2.2a1 1 0 0 1 1-.25 11.4 11.4 0 0 0 3.6.57 1 1 0 0 1 1 1V20a1 1 0 0 1-1 1A17 17 0 0 1 3 4a1 1 0 0 1 1-1h3.5a1 1 0 0 1 1 1c0 1.25.2 2.45.57 3.57a1 1 0 0 1-.25 1z"/></svg>000 111 2223</li>
      <li><svg viewBox="0 0 24 24"><path d="M2 5h20v14H2zm2 2v.5l8 5 8-5V7zm0 3v7h16v-7l-8 5z"/></svg>urname@email.com</li>
      <li><svg viewBox="0 0 24 24"><path d="M12 2a10 10 0 1 0 0 20 10 10 0 0 0 0-20zm-1 17.9A8 8 0 0 1 4 12l5 5v1a2 2 0 0 0 2 2zm6.9-2.5A2 2 0 0 0 16 16h-1v-3a1 1 0 0 0-1-1H8v-2h2a1 1 0 0 0 1-1V7h2a2 2 0 0 0 2-2v-.4a8 8 0 0 1 2.9 12.8z"/></svg>www.<span class="accent">ursitename</span>.com</li>
    </ul>
    <div class="address">
      <svg viewBox="0 0 12 16"><path d="M6 0a6 6 0 0 0-6 6c0 4.5 6 10 6 10s6-5.5 6-10a6 6 0 0 0-6-6zm0 8.2A2.2 2.2 0 1 1 6 3.8a2.2 2.2 0 0 1 0 4.4z"/></svg>
      Your Street Address, UnitedStates, 1234
    </div>
    <div class="edge-band"></div>
  </section>
</body>
</html>
```